ink nest studio nos proporciona ter várias ideias vindo de mentes criativas diferentes o que nos faz termos muito mais variedades do que se uma única pessoa criasse vários logos.

```html
<!DOCTYPE html>
<html lang="pt-BR">
<head>
<meta charset="utf-8">
<title>Assinatura de e-mail – ink nest studio</title>
<link rel="stylesheet" href="https://fonts.googleapis.com/css2?family=Open+Sans:wght@400;600;700&display=swap">
<style>
  :root {
    --bg: #f4f4f4;
    --paper: #ffffff;
    --pink: #f39ab8;
    --yellow: #f5e27c;
    --green: #a9dc8e;
    --purple: #c9a2e2;
    --cyan: #86d6ea;
    --ink: #2f3a45;
    --muted: #7a8591;
    --brand: #1f6fb2;
  }
  * { box-sizing: border-box; margin: 0; padding: 0; }
  html, body {
    width: 1200px; height: 1200px; overflow: hidden;
    background: var(--bg);
    font-family: "Open Sans", Arial, sans-serif;
    color: var(--ink);
  }
  .canvas {
    width: 1200px; height: 1200px;
    display: flex; align-items: center; justify-content: center;
  }
  .signature {
    width: 1000px;
    background: var(--paper);
    padding: 0 0 0 0;
  }
  .stripe {
    display: flex; height: 26px;
  }
  .stripe span { flex: 1; }
  .stripe .pink { background: var(--pink); }
  .stripe .yellow { background: var(--yellow); }
  .stripe .green { background: var(--green); }
  .stripe .purple { background: var(--purple); }
  .stripe .cyan { background: var(--cyan); }
  .stripe--thin { height: 12px; }
  .signature-body {
    display: flex; align-items: flex-end; justify-content: space-between;
    padding: 60px 50px 50px;
  }
  .identity { display: flex; align-items: flex-end; gap: 40px; }
  .brand {
    display: flex; flex-direction: column; align-items: flex-start; gap: 14px;
  }
  .brand-dot {
    width: 110px; height: 110px; border-radius: 50%;
    background: var(--cyan);
  }
  .brand-name {
    font-weight: 700; font-size: 34px; color: var(--brand);
    letter-spacing: 0.5px;
  }
  .person { padding-bottom: 4px; }
  .person-name { font-weight: 700; font-size: 40px; color: var(--ink); line-height: 1.1; }
  .person-role { font-size: 24px; color: var(--muted); margin-top: 6px; }
  .contacts { list-style: none; display: flex; flex-direction: column; gap: 16px; }
  .contact { display: flex; align-items: center; gap: 14px; font-size: 22px; color: var(--muted); }
  .contact-icon { width: 30px; height: 30px; flex: none; }
</style>
</head>
<body>
<main class="canvas">
  <section class="signature" aria-label="Assinatura de e-mail">
    <div class="stripe">
      <span class="pink"></span><span class="yellow"></span><span class="green"></span><span class="purple"></span><span class="cyan"></span>
    </div>
    <div class="signature-body">
      <div class="identity">
        <div class="brand">
          <div class="brand-dot"></div>
          <div class="brand-name">ink nest studio</div>
        </div>
        <div class="person">
          <p class="person-name">Nome Sobrenome</p>
          <p class="person-role">Cargo</p>
        </div>
      </div>
      <ul class="contacts">
        <li class="contact">
          <svg class="contact-icon" viewBox="0 0 30 30"><circle cx="15" cy="15" r="15" fill="#86d6ea"/><path d="M15 7a5 5 0 0 0-5 5c0 4 5 10 5 10s5-6 5-10a5 5 0 0 0-5-5zm0 7a2 2 0 1 1 0-4 2 2 0 0 1 0 4z" fill="#fff"/></svg>
          Rua Alva, 120 - Centro, SP
        </li>
        <li class="contact">
          <svg class="contact-icon" viewBox="0 0 30 30"><circle cx="15" cy="15" r="15" fill="#a9dc8e"/><path d="M11 8l3 3-2 2c1 2 3 4 5 5l2-2 3 3-2 3c-6-1-11-6-12-12z" fill="#fff"/></svg>
          (11) 3456-7890
        </li>
        <li class="contact">
          <svg class="contact-icon" viewBox="0 0 30 30"><circle cx="15" cy="15" r="15" fill="#c9a2e2"/><rect x="8" y="10" width="14" height="10" rx="1" fill="#fff"/><path d="M8 11l7 5 7-5" stroke="#c9a2e2" stroke-width="1.5" fill="none"/></svg>
          contato@inknest.com.br
        </li>
        <li class="contact">
          <svg class="contact-icon" viewBox="0 0 30 30"><circle cx="15" cy="15" r="15" fill="#f5e27c"/><rect x="11" y="7" width="8" height="16" rx="2" fill="#fff"/></svg>
          (11) 98765-4321
        </li>
        <li class="contact">
          <svg class="contact-icon" viewBox="0 0 30 30"><circle cx="15" cy="15" r="15" fill="#f39ab8"/><rect x="11" y="7" width="8" height="16" rx="2" fill="#fff"/></svg>
          (11) 91234-5678
        </li>
      </ul>
    </div>
    <div class="stripe stripe--thin">
      <span class="pink"></span><span class="yellow"></span><span class="green"></span><span class="purple"></span><span class="cyan"></span>
    </div>
  </section>
</main>
</body>
</html>
```